Tamarack Hearth Partners Business Card

Looking for a new business card layout. We are a real estate firm w/ a logo, old design attached. Must keep the same elements on there, just need a fresh look and possible some foil accents. Looking for a simpler design w/ more modern style.

Target Market(s)

Real Estate clients

Industry/Entity Type

Real Estate Agent

Contact Information for Business Card

see attached

Font styles to use
Sans Serif

Requirements
Must have
• all elements on current biz card
Nice to have
• modern look, simpler than we have!
Should not have
• no serif fonts

```html
<!DOCTYPE html>
<html lang="en">
<head>
<meta charset="utf-8">
<title>Tamarack Hearth Partners – Business Card</title>
<link rel="stylesheet" href="https://fonts.googleapis.com/css2?family=Raleway:wght@500;700&family=Noto+Sans:wght@400;500&display=swap">
<style>
  :root {
    --page: #e4e4e4;
    --card-white: #ffffff;
    --ink: #262626;
    --brand-blue: #22398f;
    --back-dark: #2c2c2c;
    --back-light: #3d3d3d;
    --white: #ffffff;
  }
  * { margin: 0; padding: 0; box-sizing: border-box; }
  html, body { width: 1052px; height: 1200px; overflow: hidden; }
  body { background: var(--page); position: relative; }

  .card { position: absolute; left: 30px; width: 995px; height: 567px; overflow: hidden; }
  .card-front { top: 24px; background: var(--card-white); }
  .card-back { top: 609px; background: linear-gradient(115deg, var(--back-dark) 0%, #303030 55%, var(--back-light) 100%); }

  .base-band { position: absolute; left: 0; bottom: 0; width: 100%; height: 40px; background: var(--brand-blue); }

  .wordmark-small { font-family: "Raleway", sans-serif; font-weight: 500; letter-spacing: 0.32em; text-transform: uppercase; white-space: nowrap; }
  .wordmark-large { font-family: "Raleway", sans-serif; font-weight: 700; text-transform: uppercase; letter-spacing: 0.01em; white-space: nowrap; }

  .front-brand { position: absolute; left: 64px; top: 26px; color: var(--ink); }
  .front-brand .wordmark-small { font-size: 24px; line-height: 32px; }
  .front-brand .wordmark-large { font-size: 60px; line-height: 66px; }

  .front-art { position: absolute; left: 0; top: 0; width: 995px; height: 567px; }

  .contact-line {
    position: absolute; right: 518px; font-family: "Noto Sans", sans-serif;
    font-size: 20px; line-height: 28px; color: var(--ink); white-space: nowrap;
  }

  .name-tag { position: absolute; left: 716px; top: 412px; width: 279px; height: 90px; }
  .name-tag .tag-shape { position: absolute; inset: 0; width: 100%; height: 100%; }
  .agent-name { position: absolute; left: 34px; top: 12px; font-family: "Noto Sans", sans-serif; font-size: 30px; line-height: 40px; color: var(--ink); white-space: nowrap; }
  .agent-title { position: absolute; left: 36px; top: 56px; font-family: "Noto Sans", sans-serif; font-weight: 500; font-size: 17px; line-height: 22px; color: var(--brand-blue); white-space: nowrap; }

  .back-brand { position: absolute; left: 0; width: 100%; text-align: center; color: var(--white); }
  .back-brand .wordmark-small { position: absolute; left: 0; width: 100%; top: 224px; font-size: 27px; line-height: 32px; }
  .back-brand .wordmark-large { position: absolute; left: 0; width: 100%; top: 258px; font-size: 66px; line-height: 76px; }
  .rule { position: absolute; top: 282px; height: 3px; width: 213px; background: var(--white); }
  .rule-left { left: 0; }
  .rule-right { right: 0; }
</style>
</head>
<body>

<section class="card card-front" aria-label="Business card front">
  <svg class="front-art" viewBox="0 0 701 399" preserveAspectRatio="none">
    <defs>
      <linearGradient id="portraitTones" x1="0" y1="0" x2="1" y2="1">
        <stop offset="0" stop-color="#d9cfc2"/>
        <stop offset="0.45" stop-color="#e0bfa0"/>
        <stop offset="0.8" stop-color="#c9a882"/>
        <stop offset="1" stop-color="#3ec4c8"/>
      </linearGradient>
    </defs>
    <polygon class="portrait-area" role="img" aria-label="Portrait photo of the broker" points="455,0 701,0 701,371 373,371" fill="url(#portraitTones)"/>
    <polygon class="accent-stripe" points="362,0 455,0 373,371 371,371 346,303" fill="var(--brand-blue)"/>
    <g class="icon-phone" fill="#fff" transform="translate(390,162)">
      <rect x="1" y="5" width="14" height="9" rx="2"/>
      <path d="M0 4 Q8 -2 16 4 L14 6 Q8 2 2 6 Z"/>
    </g>
    <g class="icon-web" fill="none" stroke="#fff" stroke-width="1.6" transform="translate(383,237)">
      <circle r="7.5"/>
      <ellipse rx="3.2" ry="7.5"/>
      <line x1="-7.5" y1="0" x2="7.5" y2="0"/>
    </g>
    <g class="icon-pin" transform="translate(367,305)">
      <path d="M0 9 C-6 1 -6 -3 -6 -4 A6 6 0 0 1 6 -4 C6 -3 6 1 0 9 Z" fill="#fff"/>
      <circle cy="-4" r="2.2" fill="var(--brand-blue)"/>
    </g>
  </svg>

  <div class="front-brand">
    <div class="wordmark-small">Tamarack Hearth</div>
    <div class="wordmark-large">Partners</div>
  </div>

  <div class="contact-line" style="top:210px">555.201.4836</div>
  <div class="contact-line" style="top:249px">555.317.9052</div>
  <div class="contact-line" style="top:304px">maren@tamarackhearth.com</div>
  <div class="contact-line" style="top:342px">TamarackHearth-Homes.com</div>
  <div class="contact-line" style="top:397px">48 Juniper Ridge Ave</div>
  <div class="contact-line" style="top:437px">Pinecrest, OR 97000</div>

  <div class="name-tag">
    <svg class="tag-shape" viewBox="0 0 279 90" preserveAspectRatio="none" aria-hidden="true">
      <polygon points="22,0 279,0 279,90 22,90 0,45" fill="#fff"/>
    </svg>
    <div class="agent-name">Maren Whitlock</div>
    <div class="agent-title">Principle Broker</div>
  </div>

  <div class="base-band"></div>
</section>

<section class="card card-back" aria-label="Business card back">
  <div class="rule rule-left"></div>
  <div class="rule rule-right"></div>
  <div class="back-brand">
    <div class="wordmark-small">Tamarack Hearth</div>
    <div class="wordmark-large">Partners</div>
  </div>
  <div class="base-band"></div>
</section>

</body>
</html>
```